New webpage design for development bureau

We are a development bureau in Denmark, and need a design for our webpage. We are called Tindral Development (Part of Tindral Brisk Skolary Group), and are going to aim for multiple markets: Web, Apps, Desktop applications, ect.

We already have a logo, see the uploaded file. We do not have any special demands, other than in have to be simple. A portfolio view should also be available, for future customers.

```html
<!DOCTYPE html>
<html lang="en">
<head>
<meta charset="utf-8">
<title>Tindral Development</title>
<link rel="stylesheet" href="https://fonts.googleapis.com/css2?family=Open+Sans:wght@400;600&family=Questrial&family=Raleway:wght@300;600;800&display=swap">
<style>
:root{
  --blue:#1a8ac6;
  --blue-dark:#136f9f;
  --ink:#333a40;
  --text:#555b60;
  --muted:#8a9096;
  --grey-btn:#8e979d;
  --line:#dde2e6;
  --bg-soft:#f4f6f8;
  --white:#ffffff;
  --footer-bar:#3b3f43;
}
*{box-sizing:border-box;margin:0;padding:0}
html,body{width:1200px;height:3220px;overflow:hidden}
body{font-family:"Open Sans",Arial,sans-serif;color:var(--text);background:var(--white);position:relative}
.abs{position:absolute}
.center{text-align:center}

/* top bar */
.topbar{top:0;left:0;width:1200px;height:47px;background:var(--blue)}
.social{display:flex;gap:8px;position:absolute;left:806px;top:11px}
.social span{width:26px;height:26px;border-radius:50%;background:var(--white);display:block}
.search{position:absolute;left:958px;top:10px;width:202px;height:28px;background:var(--white);border-radius:14px;font-size:13px;color:#999;padding:5px 14px}
.search svg{position:absolute;right:10px;top:7px}

/* nav */
.nav{top:47px;left:0;width:1200px;height:103px;background:var(--white)}
.logo{position:absolute;left:58px;top:27px;font-family:"Raleway",sans-serif;font-weight:800;font-size:44px;color:#1f2326;letter-spacing:1px}
.menu{position:absolute;right:0;top:0;display:flex}
.menu a{font-family:"Questrial",sans-serif;font-size:16px;color:#444;text-decoration:none;height:103px;line-height:98px;letter-spacing:.5px}
.menu a:nth-child(1){position:absolute;left:-825px;width:74px;text-align:center;border-bottom:5px solid var(--blue)}
.nav-links{position:absolute;top:0;left:0;width:1200px;height:103px}
.nav-links a{position:absolute;top:0;font-family:"Questrial",sans-serif;font-size:16px;color:#444;text-decoration:none;line-height:98px;letter-spacing:.5px}
.nav-links a.active{border-bottom:5px solid var(--blue);height:103px;padding:0 9px}

/* hero */
.hero{top:150px;left:0;width:1200px;height:543px;background:linear-gradient(160deg,#4a4440 0%,#3a3633 45%,#5b4030 100%)}
.hero-title{position:absolute;top:155px;width:100%;text-align:center;font-family:"Raleway",sans-serif;font-weight:300;font-size:44px;color:#e6e6e6;letter-spacing:2px}
.hero-title b{font-weight:600;color:#fff}
.hero-text{position:absolute;top:226px;left:140px;width:920px;text-align:center;font-size:16px;line-height:27px;color:#eee}
.btn-ghost{position:absolute;top:350px;left:534px;width:132px;height:36px;border:2px solid #ddd;color:#fff;font-size:13px;line-height:32px;text-align:center;letter-spacing:.5px}
.hero-rule{top:693px;left:0;width:1200px;height:9px;background:#b9c4cc}

/* section titles */
.sec-title{font-family:"Questrial",sans-serif;font-size:25px;color:var(--ink);letter-spacing:.5px}
.sec-title span{color:var(--blue)}
.sec-text{font-size:16px;line-height:27px;color:var(--text)}

/* services */
.services{top:702px;left:0;width:1200px;height:751px;background:linear-gradient(#fff,#f3f5f7)}
.svc-line{position:absolute;top:303px;left:150px;width:900px;height:2px;background:var(--line)}
.svc-node{position:absolute;top:293px;width:24px;height:24px;border-radius:50%;background:#f6f7f8;border:2px solid #ccd2d6}
.svc-arrow{position:absolute;top:282px}
.svc{position:absolute;top:211px;width:260px;text-align:center}
.svc-circle{width:188px;height:188px;margin:0 auto;border-radius:50%;background:var(--blue);border:7px solid #dfe4e8;display:flex;align-items:center;justify-content:center}
.svc h3{margin-top:38px;font-family:"Questrial",sans-serif;font-weight:400;font-size:20px;line-height:24px;color:var(--ink);letter-spacing:1px}
.svc p{margin-top:18px;font-size:15px;line-height:23px}
.btn-small{display:inline-block;margin-top:24px;width:108px;height:30px;line-height:30px;border-radius:3px;background:var(--grey-btn);color:#fff;font-size:14px;box-shadow:0 2px 0 rgba(0,0,0,.12)}
.btn-small.on{background:var(--blue)}

/* about */
.about{top:1453px;left:0;width:1200px;height:473px;background:linear-gradient(90deg,#eceff2,#e3e7ea 50%,#edf0f2)}
.about .sec-title{position:absolute;left:79px;top:60px}
.about-text{position:absolute;left:79px;top:114px;width:552px;font-size:15.5px;line-height:26.5px;text-align:justify}
.about-text p+p{margin-top:25px}
.btn-blue{position:absolute;left:79px;top:357px;width:133px;height:41px;background:var(--blue);color:#fff;font-size:13px;line-height:41px;text-align:center;letter-spacing:.5px}
.devices{position:absolute;left:665px;top:93px;width:452px;height:247px;background:linear-gradient(#c9d3da,#9fb0bc);border-radius:6px}

/* portfolio */
.portfolio{top:1926px;left:0;width:1200px;height:876px;background:var(--white)}
.tabs{position:absolute;top:177px;left:0;width:1200px;height:44px}
.tabs span{position:absolute;font-family:"Questrial",sans-serif;font-size:20px;color:#a4aab0;letter-spacing:1px;top:10px}
.tab-on{position:absolute;left:549px;top:0;width:101px;height:40px;border:2px solid #d8dde1;border-radius:8px}
.tab-on::after{content:"";position:absolute;left:42px;bottom:-10px;width:14px;height:14px;background:#fff;border-right:2px solid #d8dde1;border-bottom:2px solid #d8dde1;transform:rotate(45deg)}
.tabs span.on{color:var(--blue);left:578px}
.tile{position:absolute;width:323px;height:215px}
.tile-overlay{background:var(--blue);display:flex;align-items:center;justify-content:center}
.btn-view{padding:0 18px;height:44px;border:2px solid rgba(255,255,255,.8);border-radius:6px;background:rgba(255,255,255,.18);color:#fff;font-size:18px;line-height:40px}
.btn-all{position:absolute;left:511px;top:777px;width:185px;height:49px;border:2px solid #d3d8dc;border-radius:4px;color:#8a9096;font-size:16px;line-height:45px;text-align:center}

/* footer */
.footer{top:2802px;left:0;width:1200px;height:373px;background:var(--blue)}
.f-col{position:absolute;top:72px}
.f-col h4{font-family:"Questrial",sans-serif;font-weight:400;font-size:18px;color:#fff;letter-spacing:1px}
.f-col ul{list-style:none;margin-top:24px}
.f-col li{font-size:13.5px;color:#e9f4fb;line-height:30px}
.field{width:178px;height:29px;background:#fff;margin-top:5px;font-size:13px;color:#999;padding:5px 8px}
.field.msg{height:87px}
.btn-submit{margin-top:10px;width:95px;height:28px;background:var(--blue-dark);color:#fff;font-size:13px;line-height:28px;text-align:center}
.bottombar{top:3175px;left:0;width:1200px;height:45px;background:var(--footer-bar)}
.bottombar p{position:absolute;left:112px;top:13px;font-size:13px;color:#e0e0e0}
.bottombar .social{left:988px;top:10px}
.bottombar .social span{width:25px;height:25px}
</style>
</head>
<body>

<header class="abs topbar">
  <div class="social"><span></span><span></span><span></span><span></span></div>
  <div class="search">Keyword Search...
    <svg width="14" height="14" viewBox="0 0 14 14"><circle cx="6" cy="6" r="4.3" fill="none" stroke="#888" stroke-width="1.6"/><line x1="9.2" y1="9.2" x2="13" y2="13" stroke="#888" stroke-width="1.8"/></svg>
  </div>
</header>

<nav class="abs nav">
  <div class="logo">TINDRAL</div>
  <div class="nav-links">
    <a class="active" style="left:365px">HOME</a>
    <a style="left:494px">ABOUT US</a>
    <a style="left:643px">OUR SERVICES</a>
    <a style="left:829px">OUR PORTFOLIO</a>
    <a style="left:1030px">CONTACT US</a>
  </div>
</nav>

<section class="abs hero" role="img" aria-label="Photograph of a laptop, tablet and phone on a wooden desk, darkened">
  <h1 class="hero-title">LOREM IPSUM <b>DOLOR TITLE</b> HEADING</h1>
  <p class="hero-text">Lorem ipsum dolor sit amet, consectetur adipiscing elit. Donec scelerisque elementum consectetur. Suspendisse leo arcu, sollicitudin in fringilla vel, vehicula et mi. Praesent nec interdum velit, vel lacinia augue. Nullam mi justo, laoreet vel vestibulum ut.</p>
  <div class="btn-ghost">READ MORE</div>
</section>
<div class="abs hero-rule"></div>

<section class="abs services">
  <h2 class="sec-title center" style="margin-top:44px">Our <span>Services</span></h2>
  <p class="sec-text center" style="margin:18px auto 0;width:680px">Donec scelerisque elementum consectetur. Suspendisse leo arcu, sollicitudin in fringilla vel, vehicula et mi. Praesent nec interdum velit.</p>

  <div class="svc-line"></div>
  <div class="svc-node" style="left:419px"></div>
  <div class="svc-node" style="left:766px"></div>
  <svg class="svc-arrow" style="left:100px" width="28" height="46" viewBox="0 0 28 46"><polyline points="24,2 4,23 24,44" fill="none" stroke="#c4cbd0" stroke-width="2"/></svg>
  <svg class="svc-arrow" style="left:1072px" width="28" height="46" viewBox="0 0 28 46"><polyline points="4,2 24,23 4,44" fill="none" stroke="#c4cbd0" stroke-width="2"/></svg>

  <div class="svc" style="left:128px">
    <div class="svc-circle">
      <svg width="60" height="100" viewBox="0 0 60 100"><rect x="3" y="3" width="54" height="94" rx="9" fill="none" stroke="#fff" stroke-width="5"/><rect x="11" y="16" width="38" height="60" fill="#fff"/><circle cx="30" cy="86" r="4" fill="#fff"/></svg>
    </div>
    <h3>Mobile App<br>Development</h3>
    <p>Lorem ipsum dolor sit amet<br>consectetur adipiscing elit.<br>Donec scelerisque elem<br>entum consectetur.</p>
    <span class="btn-small">read more</span>
  </div>

  <div class="svc" style="left:473px">
    <div class="svc-circle">
      <svg width="108" height="96" viewBox="0 0 108 96"><rect x="3" y="3" width="102" height="68" rx="4" fill="none" stroke="#fff" stroke-width="5"/><rect x="11" y="11" width="86" height="52" fill="#fff"/><rect x="44" y="72" width="20" height="13" fill="#fff"/><rect x="30" y="84" width="48" height="6" rx="2" fill="#fff"/></svg>
    </div>
    <h3>Desktop<br>Applications</h3>
    <p>Lorem ipsum dolor sit amet<br>consectetur adipiscing elit.<br>Donec scelerisque elem<br>entum consectetur.</p>
    <span class="btn-small on">read more</span>
  </div>

  <div class="svc" style="left:821px">
    <div class="svc-circle">
      <svg width="110" height="96" viewBox="0 0 110 96"><rect x="3" y="13" width="96" height="62" rx="4" fill="none" stroke="#fff" stroke-width="5"/><rect x="44" y="76" width="16" height="10" fill="#fff"/><rect x="30" y="85" width="44" height="6" rx="2" fill="#fff"/><path d="M100 4 L108 12 L56 60 L46 62 L48 52 Z" fill="#fff"/><path d="M46 62 C 34 58, 22 62, 16 66" fill="none" stroke="#fff" stroke-width="4"/></svg>
    </div>
    <h3>Web Design<br>&amp; Development</h3>
    <p>Lorem ipsum dolor sit amet<br>consectetur adipiscing elit.<br>Donec scelerisque elem<br>entum consectetur.</p>
    <span class="btn-small">read more</span>
  </div>
</section>

<section class="abs about" role="img" aria-label="Faded photograph of a busy open-plan office">
  <h2 class="sec-title">About <span>Tindral</span></h2>
  <div class="about-text">
    <p>Lorem ipsum dolor sit amet, consectetur adipiscing elit. Donec scelerisque elementum consectetur. Suspendisse leo arcu, sollicitudin in fringilla vel, vehicula et mi. Praesent nec interdum velit, vel lacinia augue. Nullam mi justo, laoreet vel vestibulum ut, mollis vel turpis.</p>
    <p>Donec scelerisque elementum consectetur. Suspendisse leo arcu, sollic itudin in fringilla vel, vehicula et mi. Praesent nec interdum velit, vel lacinia augue. Nullam mi justo, laoreet vel vestibulum ut.</p>
  </div>
  <div class="btn-blue">READ MORE</div>
  <div class="devices" role="img" aria-label="Illustration of a desktop monitor, laptop, tablet and phone showing the website"></div>
</section>

<section class="abs portfolio">
  <h2 class="sec-title center" style="margin-top:46px">Our <span>Portfolio</span></h2>
  <p class="sec-text center" style="margin:14px auto 0;width:680px">Donec scelerisque elementum consectetur. Suspendisse leo arcu, sollicitudin in fringilla vel, vehicula et mi. Praesent nec interdum velit.</p>
  <div class="tabs">
    <span style="left:362px">MOBILE</span>
    <div class="tab-on"></div>
    <span class="on">WEB</span>
    <span style="left:755px">DESKTOP</span>
  </div>
  <div class="tile" style="left:101px;top:268px;background:linear-gradient(#f0e6d2,#e9dcc0)" role="img" aria-label="Project screenshot: illustrated agency website"></div>
  <div class="tile" style="left:438px;top:268px;background:linear-gradient(#1e2a38,#2c3e55)" role="img" aria-label="Project screenshot: dark website with blue content panel"></div>
  <div class="tile" style="left:773px;top:268px;background:linear-gradient(135deg,#2b2a2c,#6b4a33 60%,#b8452c)" role="img" aria-label="Project screenshot: studio portfolio site with colourful tiles"></div>
  <div class="tile" style="left:101px;top:496px;background:linear-gradient(#eeeeee 0 12%,#e2dd1e 12% 82%,#f2f2f2 82%)" role="img" aria-label="Project screenshot: website with yellow banner and dragonfly"></div>
  <div class="tile tile-overlay" style="left:438px;top:496px" role="img" aria-label="Project screenshot under blue hover overlay"><span class="btn-view">View Project</span></div>
  <div class="tile" style="left:773px;top:496px;background:linear-gradient(#1d1d1f 0 22%,#8fb43a 22% 75%,#202022 75%)" role="img" aria-label="Project screenshot: website with green landscape banner"></div>
  <div class="btn-all">View All Projects</div>
</section>

<footer class="abs footer">
  <div class="f-col" style="left:112px"><h4>ABOUT US</h4>
    <ul><li>Our Team</li><li>Testimonials</li><li>Our Partners</li></ul></div>
  <div class="f-col" style="left:326px"><h4>SERVICES OFFERED</h4>
    <ul><li>Link goes here</li><li>Link goes here</li><li>Link goes here</li><li>Link goes here</li><li>Link goes here</li></ul></div>
  <div class="f-col" style="left:608px"><h4>ADDITIONAL INFO</h4>
    <ul><li>Sitemap</li><li>FAQ</li><li>Privacy Policy</li><li>Terms &amp; Agreement</li></ul></div>
  <div class="f-col" style="left:906px"><h4>QUICK CONTACT</h4>
    <div style="margin-top:22px">
      <div class="field">Firstname</div>
      <div class="field">Email</div>
      <div class="field msg">Message</div>
      <div class="btn-submit">Submit</div>
    </div>
  </div>
</footer>

<div class="abs bottombar">
  <p>Tindral All Rights Reserved &copy; 2014</p>
  <div class="social"><span></span><span></span><span></span></div>
</div>

</body>
</html>
```